Dental Office Needs- Flyer Design for Same Day Crowns

We need a flyer that will explain the benefits of the same day crown from the patient prospective. Not show pictures of the machine that makes the crowns. See attached material for content. The flyer should use the practices PMS colors of Green 562 and Blue 3025. The ad should say to the patient - I want to go this office and get my crown done there.
Updates

Project Deadline Extended Reason: The difference in the time zone between USA and Europe has caused issues. Minor changes still need to be worked out. Added Thursday, July 14, 2016

Target Market(s)

Dental Patients

Industry/Entity Type

Dental

Requirements
Must have
• Call to Action
• Business Address and Business Logo
• Classic Design
• images of a Happy 50 year old Couple
• Gives the benefits of the same day crown
Should not have
• No Images of tooth figures
• No before or after pictures

```html
<!DOCTYPE html>
<html lang="en">
<head>
<meta charset="utf-8">
<title>Same-Day Crown Trifold</title>
<link rel="stylesheet" href="https://fonts.googleapis.com/css2?family=PT+Sans+Narrow:wght@700&family=Roboto:wght@300;400;700&display=swap">
<style>
  :root {
    --green: #22904f;
    --green-dark: #145a32;
    --teal: #1b5e6e;
    --teal-soft: #2a7a86;
    --rule: #b9d6d6;
    --paper: #ffffff;
    --edge: #d4d4d4;
  }
  * { margin: 0; padding: 0; box-sizing: border-box; }
  html, body { width: 1200px; height: 928px; overflow: hidden; background: var(--paper); }
  .brochure { position: relative; width: 1200px; height: 928px; border: 1px solid var(--edge); font-family: "Roboto", sans-serif; }
  .panel { position: absolute; top: 0; height: 928px; }

  /* Left panel */
  .panel--benefits { left: 0; width: 400px; background: var(--green); color: #fff; }
  .benefits__line { position: absolute; width: 3px; background: #fff; }
  .benefits__line--top { left: 130px; top: 0; height: 70px; }
  .benefits__line--long { left: 289px; top: 252px; bottom: 0; }
  .benefits__headline {
    position: absolute; top: 68px; left: 0; width: 400px; text-align: center;
    font-family: "PT Sans Narrow", sans-serif; font-weight: 700; font-size: 31px; line-height: 42px;
  }
  .benefit { position: absolute; left: 0; display: flex; align-items: center; }
  .benefit__bar { width: 70px; height: 4px; background: var(--green-dark); }
  .benefit__tick { width: 3px; height: 36px; background: var(--green-dark); margin-right: 14px; }
  .benefit__text { font-family: "PT Sans Narrow", sans-serif; font-weight: 700; font-size: 20px; line-height: 27px; }
  .benefit--1 { top: 490px; }
  .benefit--2 { top: 571px; }
  .benefit--3 { top: 653px; }

  /* Middle panel */
  .panel--contact { left: 400px; width: 400px; border-right: 1px solid var(--edge); }
  .contact__question {
    position: absolute; top: 224px; left: 0; width: 400px; text-align: center;
    color: var(--teal-soft); font-weight: 300; font-size: 22px; line-height: 31px;
  }
  .contact__name { position: absolute; top: 706px; left: 0; width: 400px; text-align: center; color: var(--teal); font-size: 23px; font-weight: 400; }
  .contact__tagline { position: absolute; top: 742px; left: 0; width: 400px; text-align: center; color: var(--green); font-size: 13px; }
  .contact__list { position: absolute; top: 785px; left: 44px; list-style: none; color: #3f4a4f; font-size: 15px; }
  .contact__list li { display: flex; align-items: center; height: 26px; }
  .contact__list svg { width: 15px; height: 15px; margin-right: 5px; fill: var(--green); }

  /* Right panel */
  .panel--promise { left: 800px; width: 400px; }
  .promise__brand { position: absolute; top: 86px; left: 0; width: 400px; text-align: center; color: var(--green); font-size: 16px; font-weight: 400; }
  .promise__photo {
    position: absolute; top: 190px; left: 8px; width: 392px; height: 420px;
    background: radial-gradient(ellipse at 55% 45%, #9ea8a6 0%, #c9d0ce 45%, #f2f4f3 80%, #fff 100%);
  }
  .promise__list { position: absolute; top: 628px; left: 45px; width: 311px; list-style: none; }
  .promise__item {
    text-align: center; color: var(--teal); font-weight: 700; font-size: 18px; line-height: 28px;
    padding: 2px 0 24px; border-bottom: 1px solid var(--rule); margin-bottom: 8px;
  }
  .promise__item:last-child { border-bottom: none; }
</style>
</head>
<body>
<div class="brochure">
  <section class="panel panel--benefits">
    <span class="benefits__line benefits__line--top"></span>
    <span class="benefits__line benefits__line--long"></span>
    <h1 class="benefits__headline">WHEN IT COMES<br>TO YOUR NEXT CROWN,<br>THE BENEFITS OF<br>A DIGITAL RESTORATION<br>ADD UP QUICKLY!</h1>
    <div class="benefit benefit--1"><span class="benefit__bar"></span><span class="benefit__tick"></span><p class="benefit__text">A Same-Day<br>Restoration</p></div>
    <div class="benefit benefit--2"><span class="benefit__bar"></span><span class="benefit__tick"></span><p class="benefit__text">A Stronger More<br>Precise Fit</p></div>
    <div class="benefit benefit--3"><span class="benefit__bar"></span><span class="benefit__tick"></span><p class="benefit__text">A Beautiful Natural<br>Appearance</p></div>
  </section>

  <section class="panel panel--contact">
    <p class="contact__question">Are you ready for<br>a dramatically<br>improved experience<br>with your next crown?</p>
    <p class="contact__name">Northfield Dental Studio</p>
    <p class="contact__tagline">Healthy Smiles Start Here</p>
    <ul class="contact__list">
      <li><svg viewBox="0 0 16 16"><path d="M8 0a5.5 5.5 0 0 0-5.5 5.5C2.5 9.8 8 16 8 16s5.5-6.2 5.5-10.5A5.5 5.5 0 0 0 8 0zm0 8a2.5 2.5 0 1 1 0-5 2.5 2.5 0 0 1 0 5z"/></svg>418 Cedar Ridge Ave. Brookvale, MI 48000</li>
      <li><svg viewBox="0 0 16 16"><path d="M3.6 1l2.3 3.2-1.4 1.5c.9 2 2.6 3.7 4.6 4.6l1.5-1.4L15 11.2 13.4 14C7 14 2 9 2 2.6z"/></svg>555.014.2837</li>
      <li><svg viewBox="0 0 16 16"><circle cx="8" cy="8" r="7"/></svg>www.northfielddentalstudio.com</li>
      <li><svg viewBox="0 0 16 16"><path d="M1 3h14v10H1zm1 1l6 5 6-5z"/></svg>hello@northfielddentalstudio.com</li>
    </ul>
  </section>

  <section class="panel panel--promise">
    <p class="promise__brand">Northfield Dental Studio</p>
    <div class="promise__photo" role="img" aria-label="Black and white photo of a smiling older couple embracing cheek to cheek"></div>
    <ul class="promise__list">
      <li class="promise__item">GOOD-BYE<br>TEMPORARY CROWN</li>
      <li class="promise__item">GOOD-BYE<br>SECOND APPOINTMENT</li>
      <li class="promise__item">GOOD-BYE<br>GOOEY MESSY IMPRESSIONS</li>
    </ul>
  </section>
</div>
</body>
</html>
```